Maple Row Yardcare

I want it as prefession and attractive as possible we are a lawnmowing business

Phone number 605-318-2264
Name- Carl Whitby
Email- mapleroweyardsd@fernpost.net

```html
<!DOCTYPE html>
<html lang="en">
<head>
<meta charset="utf-8">
<title>Maple Row Yardcare – Business Card</title>
<link href="https://fonts.googleapis.com/css2?family=Roboto:wght@400;700&display=swap" rel="stylesheet">
<style>
  :root {
    --page-bg: #e9e9e9;
    --card-green: #115e3a;
    --leaf-green: #5dbb46;
    --white: #ffffff;
  }
  * { margin: 0; padding: 0; box-sizing: border-box; }
  html, body {
    width: 1200px;
    height: 1200px;
    overflow: hidden;
    background: var(--page-bg);
    font-family: "Roboto", sans-serif;
  }
  .canvas { position: relative; width: 1200px; height: 1200px; }
  .card {
    position: absolute;
    left: 225px;
    width: 749px;
    height: 448px;
    background: var(--card-green);
  }
  .card-front { top: 120px; }
  .card-back { top: 631px; }

  .brand-name {
    position: absolute;
    left: 51px;
    top: 70px;
    font-family: "Roboto", sans-serif;
    font-weight: 700;
    font-size: 40px;
    letter-spacing: 0.5px;
    text-transform: uppercase;
    color: var(--leaf-green);
    white-space: nowrap;
  }
  .brand-rule {
    position: absolute;
    left: 51px;
    top: 135px;
    width: 649px;
    height: 5px;
    background: var(--white);
  }
  .holder-name {
    position: absolute;
    left: 52px;
    top: 275px;
    font-weight: 700;
    font-size: 30px;
    color: var(--white);
    text-transform: uppercase;
    letter-spacing: 0.2px;
  }
  .contact-list { position: absolute; left: 51px; top: 330px; list-style: none; }
  .contact-item {
    display: flex;
    align-items: center;
    height: 38px;
    font-size: 24px;
    color: var(--leaf-green);
  }
  .contact-icon { width: 20px; height: 20px; margin-right: 15px; flex: none; }

  .back-brand {
    position: absolute;
    inset: 0;
    display: flex;
    align-items: center;
    justify-content: center;
    font-family: "Roboto", sans-serif;
    font-weight: 700;
    font-size: 50px;
    text-transform: uppercase;
    color: var(--leaf-green);
    white-space: nowrap;
  }
</style>
</head>
<body>
<div class="canvas">
  <section class="card card-front">
    <div class="brand-name">Maple Row Yardcare</div>
    <div class="brand-rule"></div>
    <h1 class="holder-name">Carl Whitby</h1>
    <ul class="contact-list">
      <li class="contact-item">
        <svg class="contact-icon" viewBox="0 0 24 24" aria-hidden="true">
          <path fill="#fff" d="M6.6 10.8c1.4 2.8 3.8 5.1 6.6 6.6l2.2-2.2c.3-.3.7-.4 1-.2 1.1.4 2.3.6 3.6.6.6 0 1 .4 1 1V20c0 .6-.4 1-1 1C10.6 21 3 13.4 3 4c0-.6.4-1 1-1h3.5c.6 0 1 .4 1 1 0 1.3.2 2.5.6 3.6.1.3 0 .7-.2 1L6.6 10.8z"/>
        </svg>
        605-318-2264
      </li>
      <li class="contact-item">
        <svg class="contact-icon" viewBox="0 0 24 24" aria-hidden="true">
          <rect x="2" y="5" width="20" height="14" fill="#fff"/>
          <path d="M2.5 5.5 12 13l9.5-7.5M2.5 18.5l7-6.5M21.5 18.5l-7-6.5" fill="none" stroke="#115e3a" stroke-width="1.4"/>
        </svg>
        mapleroweyardsd@fernpost.net
      </li>
    </ul>
  </section>

  <section class="card card-back">
    <div class="back-brand">Maple Row Yardcare</div>
  </section>
</div>
</body>
</html>
```